ice cream shop needs flavor of the month poster

we need an A3 size poster design for the flavor of the month . we will provide you 2 ice cream images to choose from one in a cone which we personally prefer and the other one in a cup . we will also provide you our colors pantone and patterns if you would like to use it. the design should focus on the ice cream image and it should has the title of flavor of the moth and the name of the ice cream mix which is ( Nader Quince ice cream mix) .

Target Market(s)

families and 18-25

Industry/Entity Type

Cafe

Font styles to use
Other font styles liked:
• arial

Colors
eea4c8
fbf289
f68e4e
abd036

Requirements
Must have
• logo small size
• name of the mix (nader quince ice cream mix)
• title ( Flavor of the month )
Nice to have
• keep it simple

```html
<!DOCTYPE html>
<html lang="en">
<head>
<meta charset="utf-8">
<title>Flavor of the Month Poster</title>
<link rel="stylesheet" href="https://fonts.googleapis.com/css2?family=Lilita+One&display=swap">
<style>
  :root {
    --bg: #e9e7e4;
    --pink: #eea4c8;
    --white: #ffffff;
    --yellow: #f7d81c;
    --yellow-light: #fbf289;
    --orange: #f6a21e;
    --brown: #6e3f20;
    --brown-dark: #4a2a14;
    --stitch: #c98c5c;
  }
  * { margin: 0; padding: 0; box-sizing: border-box; }
  html, body { width: 1200px; height: 1148px; overflow: hidden; background: var(--bg); }
  .poster {
    position: absolute; left: 210px; top: 24px; width: 780px; height: 1100px;
    background: var(--pink); padding: 14px;
  }
  .poster-inner {
    position: relative; width: 100%; height: 100%;
    background: var(--white); padding: 6px;
  }
  .poster-field {
    position: relative; width: 100%; height: 100%; overflow: hidden;
    background: radial-gradient(ellipse at 50% 52%, var(--yellow-light) 0%, var(--yellow) 45%, var(--orange) 100%);
    font-family: "Lilita One", Arial, sans-serif;
  }
  .brand {
    position: absolute; top: 32px; left: 0; right: 0;
    text-align: center;
  }
  .brand-name { color: var(--brown); font-size: 24px; letter-spacing: 2px; text-transform: uppercase; }
  .title {
    position: absolute; top: 100px; left: 0; right: 0; text-align: center;
    color: var(--white); font-size: 104px; font-weight: 400; line-height: 0.98; letter-spacing: 1px;
    text-transform: uppercase;
  }
  .product-photo {
    position: absolute; left: 205px; top: 315px; width: 310px; height: 670px;
    border-radius: 140px 140px 20px 20px;
    background: linear-gradient(180deg, #efe6da 0%, #d8b585 45%, #c48a4c 100%);
  }
  .ribbon { position: absolute; left: 0; top: 680px; width: 736px; height: 220px; }
  .ribbon-text {
    position: absolute; left: 0; right: 0; top: 712px; text-align: center;
    color: var(--white); font-size: 50px; line-height: 0.95; text-transform: uppercase;
    transform: rotate(-4deg);
  }
</style>
</head>
<body>
  <div class="poster">
    <div class="poster-inner">
      <div class="poster-field">
        <div class="brand">
          <span class="brand-name">Honeybell Dairy</span>
        </div>
        <h1 class="title">Flavor<br>of the month</h1>
        <div class="product-photo" role="img" aria-label="Photo of a waffle cone with two scoops of ice cream, biscuit crumbs, caramel drizzle and a biscuit"></div>
        <svg class="ribbon" viewBox="0 0 736 220" aria-hidden="true">
          <polygon points="40,110 150,100 150,190 60,200 90,155" fill="var(--brown)"/>
          <polygon points="696,80 586,70 586,160 676,172 646,125" fill="var(--brown)"/>
          <polygon points="150,190 120,170 150,168" fill="var(--brown-dark)"/>
          <polygon points="586,160 616,150 586,142" fill="var(--brown-dark)"/>
          <polygon points="120,40 610,6 620,140 130,170" fill="var(--brown)"/>
          <polyline points="126,50 612,16" fill="none" stroke="var(--stitch)" stroke-width="2" stroke-dasharray="8 5"/>
          <polyline points="134,160 616,130" fill="none" stroke="var(--stitch)" stroke-width="2" stroke-dasharray="8 5"/>
        </svg>
        <div class="ribbon-text">Nader Quince<br>Ice Cream Mix</div>
      </div>
    </div>
  </div>
</body>
</html>
```